Flyer für Hausreinigung
Zielgruppe
Hausverwaltungen, Hausbesitzer.
Aufgabenstellung
Ergebnis soll ein Winword-Dokument mit einem Firmenlogo (Vorschlag: Tintenklecks hellgrün/blau verlaufend mit orangem Besen/Wischer/oder Hand - andere Ideen sind willkommen!) sein, das ich noch um Firmenname/Adresse bzw. Empfängerdaten noch vervollständigen/individualisieren kann. Es soll bunt, aber nicht überladen sein, eventuell mit Stockfotos von lachenden/glücklich schauenden aktiven Menschen sein, jung dynamisch aber nicht flippig. Folgender Text sollte darin vorkommen, Umformulierungen und andere Ideen sind hochwillkommen:
Unser Ziel ist es eine Hausbetreuung fast wie ein Hausbesorger zu leisten, jedoch mit zusätzlichen Vorteilen:
· Der Vertrag ist jederzeit ohne Frist kündbar, ohne Angabe von Gründen!
· Reinigung 1 x pro Woche sowie zusätzliche Bedarfsreinigung
· Krankheits- und Urlaubsvertretung sind bereits inklusive.
· Haftpflichtversicherung über 1,5 Mio. Euro
· Inklusive Gartenbetreuung, Garage, Dachboden, Haustechnik
· Kontrollgänge, 7 x 24 h Erreichbarkeit für Mieter und Eigentümer, Handwerkerüberwachung, Notfallkoordination
· Winterbetreuung der Gehsteige täglich mindestens zwischen 6:00 und 22:00
· Inklusive aller Hilfsmittel und Materialien
· Fixpreis pro Monat.
Nach Möglichkeit soll das auf 1 A4-Seite Platz finden.

```html
<!DOCTYPE html>
<html lang="de">
<head>
<meta charset="utf-8">
<title>Hausbetreuung Harald Moser – Flyer</title>
<link rel="stylesheet" href="https://fonts.googleapis.com/css2?family=Cabin:wght@500;600;700&display=swap">
<style>
  :root {
    --sky-top: #9db6d4;
    --sky-low: #cad7e3;
    --treeline: #8f9a78;
    --asphalt-light: #77726c;
    --asphalt-dark: #4a4642;
    --brand-grey: #5a5a5c;
    --accent-orange: #ee6a1e;
    --panel-white: rgba(255, 255, 255, 0.74);
    --text-dark: #444446;
    --white: #ffffff;
  }
  * { margin: 0; padding: 0; box-sizing: border-box; }
  html, body { width: 848px; height: 1200px; overflow: hidden; background: #ffffff; }
  .flyer {
    position: relative;
    width: 848px;
    height: 1200px;
    overflow: hidden;
    font-family: "Cabin", "Segoe UI", sans-serif;
  }
  .scene-photo {
    position: absolute;
    inset: 0;
    background: linear-gradient(180deg,
      var(--sky-top) 0%,
      var(--sky-low) 40%,
      var(--treeline) 48%,
      var(--asphalt-light) 54%,
      #66615c 75%,
      var(--asphalt-dark) 100%);
  }
  .brand {
    position: absolute;
    left: 96px;
    top: 46px;
    display: flex;
    align-items: center;
    gap: 44px;
  }
  .brand-mark {
    width: 150px;
    height: 150px;
    border-radius: 50%;
    background: var(--white);
  }
  .brand-name {
    color: var(--brand-grey);
    font-weight: 600;
    font-size: 34px;
    line-height: 44px;
  }
  .brand-name span { display: block; letter-spacing: 4px; }
  .brand-name span:first-child { letter-spacing: 0.5px; }
  .claim-band {
    position: absolute;
    left: -40px;
    top: 298px;
    width: 640px;
    height: 96px;
    background: var(--accent-orange);
    border-radius: 0 48px 48px 0;
    transform: rotate(-7deg);
    transform-origin: left center;
    display: flex;
    align-items: center;
    padding-left: 62px;
  }
  .claim-band p {
    color: var(--white);
    font-weight: 600;
    font-size: 23px;
    line-height: 31px;
  }
  .benefits-panel {
    position: absolute;
    left: 66px;
    top: 425px;
    width: 540px;
    height: 531px;
    background: var(--panel-white);
    border-radius: 14px;
    padding: 22px 20px 0 30px;
  }
  .benefits-list { list-style: none; }
  .benefits-list li {
    position: relative;
    padding-left: 32px;
    color: var(--text-dark);
    font-weight: 600;
    font-size: 21px;
    line-height: 30.5px;
  }
  .benefits-list li::before {
    content: "·";
    position: absolute;
    left: 0;
    top: 0;
  }
  .contact-line {
    position: absolute;
    left: 46px;
    top: 1134px;
    color: var(--white);
    font-weight: 600;
    font-size: 20px;
    letter-spacing: 0.2px;
  }
</style>
</head>
<body>
<main class="flyer">
  <div class="scene-photo" role="img" aria-label="Foto: Mann im Nadelstreifenanzug saugt mit einem Staubsauger ein Flachdach, im Hintergrund blauer Himmel und Bäume"></div>

  <header class="brand">
    <div class="brand-mark"></div>
    <div class="brand-name">
      <span>Hausbetreuung</span>
      <span>Harald Moser</span>
    </div>
  </header>

  <div class="claim-band">
    <p>Unser Ziel ist es eine Hausbetreuung wie ein Hausbe-<br>sorger zu leisten, jedoch mit zusätzlichen Vorteilen:</p>
  </div>

  <section class="benefits-panel">
    <ul class="benefits-list">
      <li>Der Vertrag ist jederzeit ohne Frist kündbar, ohne Angabe von Gründen!</li>
      <li>Reinigung 1 x pro Woche sowie zusätzliche Bedarfsreinigung</li>
      <li>Krankheits- und Urlaubsvertretung sind bereits inklusive.</li>
      <li>Haftpflichtversicherung über 1,5 Mio. Euro</li>
      <li>Inklusive Gartenbetreuung, Garage, Dachboden, Haustechnik</li>
      <li>Kontrollgänge, 7 x 24 h Erreichbarkeit für Mieter und Eigentümer, Handwerker-überwachung, Notfallkoordination</li>
      <li>Winterbetreuung der Gehsteige täglich mindestens zwischen 6:00 und 22:00</li>
      <li>Inklusive aller Hilfsmittel und Materialien</li>
      <li>Fixpreis pro Monat.</li>
    </ul>
  </section>

  <footer class="contact-line">Glanzweg 7 | 99999 Putzdorf | Tel: 0123 98 76 54-0 | Fax: 0123 98 76 54-00</footer>
</main>
</body>
</html>
```